modern design for software startup

We need a website design. We are a software company developing a cruise management system for cruise ships. We don't want or need something elaborate. In fact, we don't want to show specifics of our products because they are under development and we do not want our competitors to know too much. We want to focus on ideals and principals of our company and hint at what we are doing.

Target Market(s)

cruise lines

Industry/Entity Type

Software

Coding

Coded - Design and coding required

Number of Pages Required

1 page

Font styles to use
Sans Serif

Colors
7f7f7f
5c5c5c

Requirements
Must have
• background pictures of cruise ships, ports, ocean, some developers working on computers in brown and white and fuzzy. can't show specific cruise lines. magazine like style. white text. links at bottom to facebook, twitter, instagram
• email link for investor/partner inquiries.
Nice to have
• Some inspirational quotes here and there. Not overpowering but subtle. content to be provided in text file.
• color schemes - we like the scheme in www.tindelmarsh.com
• doesnt have to be exact but similar is good.

```html
<!DOCTYPE html>
<html lang="en">
<head>
<meta charset="utf-8">
<title>Corvane Software</title>
<link rel="stylesheet" href="https://fonts.googleapis.com/css2?family=Jura:wght@400;500;700&family=PT+Sans:wght@400;700&family=Open+Sans:wght@400;600&display=swap">
<style>
:root{
  --blue:#0b5aa6;
  --sky:#1ea0e0;
  --navy:#2b3f6b;
  --ice:#e3f3fb;
  --ink:#222;
  --grey:#5c5c5c;
  --soft:#7f7f7f;
  --footer:#ececec;
  --black:#000;
  --white:#fff;
}
*{box-sizing:border-box;margin:0;padding:0}
html,body{width:1200px;height:2647px;overflow:hidden;background:var(--white)}
body{position:relative;font-family:"PT Sans",sans-serif;color:var(--grey)}
.abs{position:absolute}
.heading{font-family:"Jura",sans-serif;font-weight:500;text-align:center;color:var(--grey)}
.heading span{color:var(--blue)}

/* header */
.topline{left:0;top:0;width:1200px;height:5px;background:var(--blue)}
.social{left:78px;top:22px;display:flex;gap:12px}
.diamond{width:50px;height:50px}
.callus{right:90px;top:20px;display:flex;align-items:center;gap:14px;font-size:23px;color:var(--soft)}
.callus .ring{width:50px;height:50px;border:2px solid var(--blue);border-radius:50%;display:flex;align-items:center;justify-content:center}
.nav{left:0;top:95px;width:1200px;height:51px;background:var(--black)}
.nav a{position:absolute;top:14px;color:var(--white);text-decoration:none;font-size:19px;text-transform:uppercase}
.brand{left:441px;top:5px;width:318px;height:141px;background:var(--white);display:flex;align-items:center;justify-content:center;gap:10px;white-space:nowrap}
.brand .mark{width:22px;height:22px;background:var(--blue);flex:none}
.brand .name{font-family:"PT Sans",sans-serif;font-weight:700;font-size:27px;color:var(--blue);letter-spacing:1px}

/* hero */
.hero{left:0;top:146px;width:1200px;height:574px;background:linear-gradient(180deg,#6a7a86 0%,#c9a060 45%,#e6b56a 55%,#3b3c36 75%,#1d1f1c 100%)}
.hero h1{position:absolute;left:78px;top:212px;font-family:"Jura",sans-serif;font-weight:700;font-size:58px;color:var(--black);white-space:nowrap}
.hero p{position:absolute;left:78px;top:292px;width:540px;font-size:24px;line-height:33px;color:var(--white)}
.hero .join{position:absolute;left:78px;top:420px;width:155px;height:46px;background:var(--white);color:var(--ink);font-size:21px;display:flex;align-items:center;justify-content:center}
.dots{position:absolute;left:560px;top:536px;display:flex;gap:6px}
.dots i{width:15px;height:15px;border:2px solid var(--white);border-radius:50%}
.dots i:first-child{background:var(--black);border-color:var(--black)}

/* welcome */
.welcome-title{left:0;top:764px;width:1200px;font-size:46px}
.screen{left:78px;top:838px;width:362px;height:304px;background:linear-gradient(180deg,#f2f4f7,#c9ced6)}
.welcome-text{left:478px;top:850px;width:640px;font-family:"Open Sans",sans-serif;font-size:15.5px;line-height:25px;color:var(--grey)}
.welcome-text p+p{margin-top:12px}
.readmore{left:476px;top:1062px;width:155px;height:45px;background:var(--blue);color:var(--white);font-size:21px;display:flex;align-items:center;justify-content:center;border-radius:3px}

/* mission */
.mission{left:0;top:1142px;width:1200px;height:240px;background:linear-gradient(180deg,#0f2530,#1f3d49 50%,#0d1f27)}
.mission h2{position:absolute;left:0;top:48px;width:1200px;font-size:46px;color:var(--white)}
.mission h2 span{color:var(--sky)}
.mission p{position:absolute;left:140px;top:128px;width:920px;text-align:center;font-family:"Open Sans",sans-serif;font-size:23px;line-height:34px;color:var(--white)}

/* who */
.who-title{left:0;top:1430px;width:1200px;font-size:46px}
.who-text{left:180px;top:1507px;width:840px;text-align:center;font-family:"Open Sans",sans-serif;font-size:14.5px;line-height:25px;color:var(--grey)}
.who-text p+p{margin-top:25px}

/* newsletter */
.newsletter{left:0;top:1739px;width:1200px;height:106px;background:var(--ice)}
.newsletter svg{position:absolute;left:0;top:0}
.newsletter h3{position:absolute;left:80px;top:24px;font-family:"Jura",sans-serif;font-weight:500;font-size:46px;color:var(--white)}
.field{position:absolute;top:30px;height:45px;background:var(--ice);border:1px solid #b9d6e6;font-family:"Open Sans",sans-serif;font-size:15px;color:var(--grey);padding:12px 12px}
.submit{position:absolute;left:998px;top:30px;width:124px;height:45px;background:var(--navy);color:var(--white);font-size:16px;display:flex;align-items:center;justify-content:center;border-radius:3px}

/* planet */
.planet-title{left:0;top:1886px;width:1200px;font-size:48px;color:var(--ink)}
.planet-photo{left:85px;top:1963px;width:268px;height:201px;background:linear-gradient(180deg,#dfe6ee,#b9c8d8)}
.planet-text{left:438px;top:1982px;width:690px;font-family:"Open Sans",sans-serif;font-size:15.5px;line-height:25px;color:var(--grey)}

/* footer */
.footer{left:0;top:2203px;width:1200px;height:397px;background:var(--footer)}
.footer h4{position:absolute;top:50px;font-family:"Jura",sans-serif;font-weight:500;font-size:27px;color:var(--blue)}
.links{position:absolute;left:79px;top:100px;list-style:none;font-family:"Open Sans",sans-serif;font-size:17px;line-height:27px;color:var(--soft)}
.news{position:absolute;left:476px;width:290px;font-family:"Open Sans",sans-serif}
.news small{display:block;font-size:12px;color:var(--soft)}
.news b{display:block;font-weight:400;font-size:19px;color:var(--blue);margin:2px 0 4px}
.news p{font-size:14px;line-height:23px;color:var(--soft)}
.news-rule{position:absolute;left:476px;top:2413px;width:290px;height:1px;background:#ccc}
.viewall{left:541px;top:2531px;font-family:"Open Sans",sans-serif;font-size:16px;color:var(--navy);text-decoration:underline}
.contact{position:absolute;left:818px;font-family:"Open Sans",sans-serif;font-size:14.5px;line-height:22px;color:var(--soft);display:flex;gap:12px}
.contact svg{flex:none;margin-top:3px}
.foot-social{left:872px;top:2454px;display:flex;gap:8px}
.foot-social svg{width:64px;height:64px}
.copy{left:0;top:2600px;width:1200px;height:47px;background:var(--black);color:var(--white);font-family:"Open Sans",sans-serif;font-size:13px;display:flex;align-items:center;justify-content:center}
.copy strong{font-weight:600;margin:0 4px}
</style>
</head>
<body>

<div class="abs topline"></div>

<div class="abs social" aria-label="Social links">
  <svg class="diamond" viewBox="0 0 50 50"><rect x="10" y="10" width="30" height="30" transform="rotate(45 25 25)" fill="var(--blue)"/></svg>
  <svg class="diamond" viewBox="0 0 50 50"><rect x="10" y="10" width="30" height="30" transform="rotate(45 25 25)" fill="none" stroke="var(--blue)" stroke-width="2"/></svg>
  <svg class="diamond" viewBox="0 0 50 50"><rect x="10" y="10" width="30" height="30" transform="rotate(45 25 25)" fill="none" stroke="var(--blue)" stroke-width="2"/></svg>
</div>

<div class="abs callus">
  <span>Call Us Now :</span>
  <span class="ring"><svg width="24" height="24" viewBox="0 0 24 24"><path d="M6 3l4 4-2 3c1 2 3 4 5 5l3-2 4 4-3 3C10 20 4 14 3 6z" fill="none" stroke="var(--blue)" stroke-width="1.6"/></svg></span>
  <span>555 010 4477</span>
</div>

<nav class="abs nav">
  <a style="left:82px">Home</a>
  <a style="left:192px">About</a>
  <a style="left:307px">Services</a>
  <a style="left:801px">Mission</a>
  <a style="left:931px">News</a>
  <a style="left:1037px">Contact</a>
</nav>

<div class="abs brand">
  <span class="mark"></span>
  <span class="name">CORVANE SOFTWARE</span>
</div>

<section class="abs hero" role="img" aria-label="Cruise ship moored in a harbour at sunset with a city skyline">
  <h1>CORVANE SOFTWARE</h1>
  <p>Courageously leading our customers, partners, and ourselves to success by caring, thinking, and doing.</p>
  <div class="join">JOIN US</div>
  <div class="dots"><i></i><i></i><i></i><i></i></div>
</section>

<h2 class="abs heading welcome-title">Welcome to <span>Corvane Software</span></h2>
<div class="abs screen" role="img" aria-label="Desktop monitor showing the company name"></div>
<div class="abs welcome-text">
  <p>What happens when you combine years of industry technical expertise, new technologies, and a strong management vision to create fresh new software in a fast moving industry currently relying on outdated tools?</p>
  <p>Our senior leadership team's focus on the big picture and how our decisions impact our people, customers, partners and our planet sets us apart. We champion our team to challenge the status Quo and to set new standards to change the way business is done and to instill Optimism in everyone.</p>
</div>
<div class="abs readmore">READ MORE</div>

<section class="abs mission" role="img" aria-label="Dark ocean waves">
  <h2 class="heading">Our <span>Mission</span></h2>
  <p>Courageously leading our customers, partners, and ourselves to success by caring, thinking, and doing.</p>
</section>

<h2 class="abs heading who-title">Who <span>We Are?</span></h2>
<div class="abs who-text">
  <p>We empower our Corvane family to speak their mind and share their ideas, no matter how outside the box or crazy they are. We champion our team to challenge the status Quo and to set new standards to change the way business is done and to instill Optimism in everyone.</p>
  <p>Our senior leadership team's focus on the big picture and how our decisions impact our people, customers, partners and our planet sets us apart. Our clear vision on business standards and being accountable to our people ensures that our people live up to exceptional standards to drive us and out customers forward while being accountable for them, each other and our the environment.</p>
</div>

<section class="abs newsletter">
  <svg width="422" height="106" viewBox="0 0 422 106"><polygon points="0,0 380,0 422,53 380,106 0,106" fill="var(--navy)"/></svg>
  <h3>Newsletter</h3>
  <div class="field" style="left:487px;width:245px">Enter Name</div>
  <div class="field" style="left:742px;width:245px">Enter E mail</div>
  <div class="submit">SUBMIT</div>
</section>

<h2 class="abs heading planet-title">Corvane's Commitment to <span>our planet</span></h2>
<div class="abs planet-photo" role="img" aria-label="Photo of two hands holding the Earth"></div>
<p class="abs planet-text">Technology is one of the largest contributor of pollution on our planet. According to the US EPA, more than 4.6 million tonnes of e-waste ended up in US landfills in 2000. Toxic chemicals in electronics products can leach into the land over time or are released into the atmosphere, impacting nearby communities and the environment. Our technology's benefit is that it works not only on the latest devices, it works on legacy systems allowing our clients to maintain older functioning technology longer keeping it our of land fills longer.</p>

<footer class="abs footer">
  <h4 style="left:79px">Useful Links</h4>
  <ul class="links"><li>Home</li><li>About</li><li>Services</li><li>News</li><li>Contact</li></ul>

  <h4 style="left:476px">Latest News</h4>
  <div class="news" style="top:100px"><small>18 Sep 2015</small><b>News Title</b><p>Lorem Ipsum is simply dummy text of the printing and typesetting industry.</p></div>
  <div class="news" style="top:226px"><small>18 Sep 2015</small><b>News Title</b><p>Lorem Ipsum is simply dummy text of the printing and typesetting industry.</p></div>

  <h4 style="left:831px">Contact Info</h4>
  <div class="contact" style="top:97px;width:230px">
    <svg width="14" height="18" viewBox="0 0 14 18"><path d="M7 0a7 7 0 0 1 7 7c0 5-7 11-7 11S0 12 0 7a7 7 0 0 1 7-7z" fill="var(--soft)"/><circle cx="7" cy="7" r="2.5" fill="var(--footer)"/></svg>
    <span>123, Lorem Ipsum,State Country,Zip Code.</span>
  </div>
  <div class="contact" style="top:150px">
    <svg width="16" height="16" viewBox="0 0 24 24"><path d="M6 3l4 4-2 3c1 2 3 4 5 5l3-2 4 4-3 3C10 20 4 14 3 6z" fill="var(--soft)"/></svg>
    <span>555 010 4477</span>
  </div>
  <div class="contact" style="top:182px">
    <svg width="18" height="14" viewBox="0 0 18 14"><rect x="1" y="1" width="16" height="12" fill="none" stroke="var(--soft)" stroke-width="1.5"/><path d="M1 1l8 7 8-7" fill="none" stroke="var(--soft)" stroke-width="1.5"/></svg>
    <span>hello@corvanesoftware.example</span>
  </div>
</footer>
<div class="abs news-rule"></div>
<div class="abs viewall">View All</div>

<div class="abs foot-social" aria-label="Social links">
  <svg viewBox="0 0 64 64"><rect x="12" y="12" width="40" height="40" transform="rotate(45 32 32)" fill="var(--black)"/></svg>
  <svg viewBox="0 0 64 64"><rect x="12" y="12" width="40" height="40" transform="rotate(45 32 32)" fill="none" stroke="var(--ink)" stroke-width="1.5"/></svg>
  <svg viewBox="0 0 64 64"><rect x="12" y="12" width="40" height="40" transform="rotate(45 32 32)" fill="none" stroke="var(--ink)" stroke-width="1.5"/></svg>
</div>

<div class="abs copy">© <strong>CORVANE SOFTWARE</strong> - 2016 All Right Reserved</div>

</body>
</html>
```